Birchby Candles, Hand-poured scented soy candles

Create a logo and label design to use on my vintage country farmhouse style, all natural, hand poured soy candle jars and apothecaries. Candles will be labeled in 4 different sizes so design must be adaptable, clean, simple, telegraphic and invoke interest in the product. Think Black lettering on white or black on kraft brown. 603 is the area code for New Hampshire where we make them. The labels will need a prominent area for the scent of the candle to be listed that the eyes are drawn to. Primitive country in design? Use of state attractions? Jars are a square mason style 8 ounce and 16 ounce. Tarts are a clamshell. Lids are a 70-400 series 2.5" label area. Candles are white in a clear glass jar, black lids. There will be label design sizes of 3"x 2.5" 2.5" round, 1.5"x2.5"

Target Market(s)

primitive country, farmhouse, vintage, general home decor

Contact Information for Business Card

Birchby Candles, all natural soy candles, hand-poured in New Hampshire, logo, phone, address. Possibly match the main label.

Logo Text

Birchby Candles, all natural soy candles, hand-poured in New Hampshire, area for scent description and size of container.

Font styles to use
Serif
Script

Colors

Designer to choose colors to be used in the design.

Requirements
Must have
• simple and clean, country farmhouse with a bit of vintage thrown in. possibly multiple fonts to distinguish info from scent name
Nice to have
• at this time I am open to suggestions
• Prefer scent names or brand name in an older script?
• older copperplate/Spencerian?
Should not have
• cluttered, busy, too modern, multiple colors

```html
<!DOCTYPE html>
<html lang="en">
<head>
<meta charset="utf-8">
<title>Birchby Candles – Jar Label and Lid Label</title>
<link href="https://fonts.googleapis.com/css2?family=Marcellus&family=Pinyon+Script&display=swap" rel="stylesheet">
<style>
  :root {
    --ink: #141213;
    --paper: #f7f7f7;
    --stage: #eeeef0;
    --sketch-light: #e4e4e4;
    --sketch-dark: #8c8c8c;
  }
  * { margin: 0; padding: 0; box-sizing: border-box; }
  html, body { width: 1200px; height: 1123px; overflow: hidden; }
  body {
    background: var(--stage);
    font-family: "Marcellus", Georgia, serif;
    color: var(--ink);
    position: relative;
  }

  /* Round lid label */
  .lid-label {
    position: absolute;
    left: 70px;
    top: 330px;
    width: 420px;
    height: 420px;
    border-radius: 50%;
    background: var(--paper);
    border: 2px solid var(--ink);
    display: flex;
    align-items: center;
    justify-content: center;
  }
  .lid-label__disc {
    width: 370px;
    height: 370px;
    border-radius: 50%;
    background: var(--ink);
    color: var(--paper);
    display: flex;
    align-items: center;
    justify-content: center;
    text-align: center;
  }
  .brand-name {
    font-family: "Marcellus", Georgia, serif;
    font-weight: 400;
    letter-spacing: 0.12em;
    text-transform: uppercase;
    line-height: 1.15;
  }
  .lid-label .brand-name { font-size: 46px; }

  /* Rectangular jar label */
  .jar-label {
    position: absolute;
    left: 540px;
    top: 310px;
    width: 600px;
    height: 500px;
    background: var(--paper);
    border: 1px solid #cfcfcf;
    border-radius: 6px;
    display: flex;
    flex-direction: column;
    align-items: center;
  }
  .jar-label__tagline {
    margin-top: 24px;
    font-size: 22px;
    letter-spacing: 0.16em;
    text-transform: uppercase;
  }
  .jar-label__rule {
    width: 100%;
    height: 10px;
    background: var(--ink);
  }
  .jar-label__rule--top { margin-top: 14px; }
  .jar-label__rule--bottom { margin-top: auto; margin-bottom: 0; }
  .brand-block {
    background: var(--ink);
    color: var(--paper);
    padding: 14px 26px 16px;
    border: 2px dotted var(--ink);
    outline: 2px dotted var(--ink);
    outline-offset: 4px;
    text-align: center;
  }
  .brand-block .brand-name { font-size: 24px; }
  .house-sketch {
    margin-top: 30px;
    width: 270px;
    height: 150px;
    border-radius: 40% 40% 20% 20%;
    background: radial-gradient(ellipse at 50% 55%, var(--sketch-dark) 0%, var(--sketch-light) 65%, var(--paper) 100%);
  }
  .scent-name {
    font-family: "Pinyon Script", cursive;
    font-size: 58px;
    line-height: 1;
    margin-top: 4px;
  }
  .jar-label__origin {
    width: 440px;
    margin-top: 6px;
    padding: 6px 0;
    border-top: 2px dashed var(--ink);
    border-bottom: 2px dashed var(--ink);
    text-align: center;
    font-size: 19px;
    letter-spacing: 0.12em;
    text-transform: uppercase;
  }
  .jar-label__dots {
    margin-top: 6px;
    font-size: 16px;
    letter-spacing: 0.3em;
    line-height: 1;
  }
  .jar-label__size {
    font-size: 17px;
    letter-spacing: 0.08em;
    margin-bottom: 8px;
  }
</style>
</head>
<body>
  <section class="lid-label" aria-label="Round lid label">
    <div class="lid-label__disc">
      <span class="brand-name">Birchby<br>Candles</span>
    </div>
  </section>

  <section class="jar-label" aria-label="Jar label">
    <p class="jar-label__tagline">All Natural Soy Candles</p>
    <div class="jar-label__rule jar-label__rule--top"></div>
    <div class="brand-block">
      <span class="brand-name">Birchby<br>Candles</span>
    </div>
    <div class="house-sketch" role="img" aria-label="Ink sketch of a country farmhouse among shrubs"></div>
    <p class="scent-name">Flavour</p>
    <p class="jar-label__origin">Hand-poured in New Hampshire</p>
    <p class="jar-label__dots">...</p>
    <p class="jar-label__size">8 oz</p>
    <div class="jar-label__rule jar-label__rule--bottom"></div>
  </section>
</body>
</html>
```